Bright Arch Group business card

Bright Arch Group is the parent company of Bright Arch Building, Bright Arch Plumbing and Bright Arch Renovating. We require a sophisticated business card that covers all aspects of the building and plumbing space without using told or construction items.

Industry/Entity Type

Construction Company

Contact Information for Business Card

Gareth Pimley
Director
0472915083
gareth@brightarch.com.au
Www.brightarch.com.au

Font styles to use
Serif
Sans Serif

Colors
3176b5
ffce3e
0692cd
34a7d8
fbee3e
faa54b

Requirements
Must have
• Logo on front
• Logo and details on rear.
Nice to have
• Maybe water mark or shadow effect with logo
Should not have
• Tools or any construction associated items

```html
<!DOCTYPE html>
<html lang="en">
<head>
<meta charset="utf-8">
<title>Bright Arch Group – Business Card</title>
<link href="https://fonts.googleapis.com/css2?family=Josefin+Sans:wght@300;400;700&display=swap" rel="stylesheet">
<style>
  :root {
    --stage: #6b7472;
    --card: #ffffff;
    --tint: #fcf1e6;
    --ink: #1f1f1f;
    --ink-soft: #3a3a3a;
    --accent: #ef7a23;
    --rule: #8a8a8a;
  }
  * { box-sizing: border-box; margin: 0; padding: 0; }
  html, body { width: 1200px; height: 800px; overflow: hidden; }
  body {
    background: var(--stage);
    font-family: "Josefin Sans", "Century Gothic", sans-serif;
    color: var(--ink);
    display: flex;
    flex-direction: column;
    align-items: center;
    justify-content: center;
    gap: 36px;
  }
  .card {
    position: relative;
    width: 640px;
    height: 366px;
    background: var(--card);
    overflow: hidden;
    box-shadow: 0 10px 28px rgba(0,0,0,.25);
  }
  .card-wash {
    position: absolute;
    inset: 0;
    background: linear-gradient(125deg, var(--tint) 0%, var(--card) 45%, var(--card) 70%, var(--tint) 100%);
  }

  /* Front */
  .brand {
    position: absolute;
    left: 50%; top: 50%;
    transform: translate(-50%, -50%);
    display: flex;
    align-items: center;
    gap: 16px;
  }
  .brand-dot {
    width: 28px; height: 28px;
    border-radius: 50%;
    background: var(--accent);
    flex: none;
  }
  .brand-name {
    font-weight: 400;
    font-size: 28px;
    letter-spacing: .28em;
    text-transform: uppercase;
    color: var(--ink);
    white-space: nowrap;
  }

  /* Back */
  .brand-small {
    position: absolute;
    right: 40px; top: 34px;
    display: flex;
    align-items: center;
    gap: 10px;
  }
  .brand-small .brand-dot { width: 14px; height: 14px; }
  .brand-small .brand-name { font-size: 14px; letter-spacing: .26em; }

  .person { position: absolute; left: 56px; top: 112px; }
  .person-name { font-weight: 700; font-size: 36px; color: var(--ink); white-space: nowrap; }
  .person-role {
    margin-top: 6px;
    font-weight: 300;
    font-size: 17px;
    letter-spacing: .38em;
    color: var(--ink-soft);
  }
  .divider {
    position: absolute;
    left: 346px; top: 96px;
    width: 1px; height: 120px;
    background: var(--rule);
  }
  .contacts {
    position: absolute;
    left: 372px; top: 118px;
    list-style: none;
    display: flex; flex-direction: column; gap: 18px;
  }
  .contact { display: flex; align-items: center; gap: 12px; font-size: 16px; color: var(--ink); white-space: nowrap; }
  .contact-icon {
    width: 26px; height: 26px; border-radius: 50%;
    background: var(--accent);
    display: flex; align-items: center; justify-content: center;
    flex: none;
  }
  .website {
    position: absolute;
    left: 56px; bottom: 52px;
    font-weight: 300;
    font-size: 17px;
    letter-spacing: .34em;
    color: var(--ink);
  }
</style>
</head>
<body>

  <section class="card card-front" aria-label="Card front">
    <div class="card-wash" role="img" aria-label="Soft peach decorative background"></div>
    <div class="brand">
      <span class="brand-dot"></span>
      <span class="brand-name">Bright Arch Group</span>
    </div>
  </section>

  <section class="card card-back" aria-label="Card back">
    <div class="card-wash" role="img" aria-label="Soft peach decorative background"></div>

    <div class="brand brand-small" style="left:auto; top:34px; transform:none;">
      <span class="brand-dot"></span>
      <span class="brand-name">Bright Arch Group</span>
    </div>

    <div class="person">
      <p class="person-name">Gareth Pimley</p>
      <p class="person-role">Director</p>
    </div>

    <span class="divider"></span>

    <ul class="contacts">
      <li class="contact">
        <span class="contact-icon">
          <svg width="13" height="13" viewBox="0 0 24 24" aria-hidden="true"><path fill="#fff" d="M6.6 10.8a15.1 15.1 0 0 0 6.6 6.6l2.2-2.2c.3-.3.7-.4 1-.2 1.1.4 2.3.6 3.6.6.6 0 1 .4 1 1V20c0 .6-.4 1-1 1A17 17 0 0 1 3 4c0-.6.4-1 1-1h3.5c.6 0 1 .4 1 1 0 1.2.2 2.4.6 3.6.1.3 0 .7-.2 1z"/></svg>
        </span>
        <span>0472915083</span>
      </li>
      <li class="contact">
        <span class="contact-icon">
          <svg width="13" height="13" viewBox="0 0 24 24" aria-hidden="true"><path fill="#fff" d="M3 5h18v14H3z"/><path fill="none" stroke="#ef7a23" stroke-width="2" d="M3 6l9 7 9-7"/></svg>
        </span>
        <span>gareth@brightarch.com.au</span>
      </li>
    </ul>

    <p class="website">www.brightarch.com.au</p>
  </section>

</body>
</html>
```